Business card design needed for Renewable utilities company based in New Zealand.

We supply and install solar panels and all components along with it for a fully customisable PV system that helps customer save money on their energy bills right away and also save the planet!

I have attached logo & website design files to give you a better insight.

Industry/Entity Type

Business

```html
<!DOCTYPE html>
<html lang="en">
<head>
<meta charset="utf-8">
<title>Clearsky Power – Business Card</title>
<link href="https://fonts.googleapis.com/css2?family=Quicksand:wght@500&family=Open+Sans:wght@400;600&display=swap" rel="stylesheet">
<style>
  :root {
    --stage: #e9e7e3;
    --blue-deep: #1c4282;
    --blue-mid: #2c5ea6;
    --blue-light: #3fa0dd;
    --navy: #1b2a66;
    --ink: #2a2a2a;
    --grey: #7a7a7a;
    --paper: #fbfbfb;
    --faint: #e6ebf2;
  }
  * { margin: 0; padding: 0; box-sizing: border-box; }
  html, body { width: 1200px; height: 1023px; overflow: hidden; background: var(--stage); }
  .canvas { position: relative; width: 1200px; height: 1023px; }

  .card {
    position: absolute;
    width: 640px;
    height: 366px;
    border-radius: 3px;
    overflow: hidden;
    box-shadow: 0 6px 18px rgba(0,0,0,0.18);
  }

  /* Back of card */
  .card-back {
    left: 140px; top: 90px;
    background: radial-gradient(ellipse at 55% 40%, var(--blue-mid) 0%, var(--blue-deep) 80%);
    color: #fff;
    text-align: center;
  }
  .world-map {
    position: absolute; left: 80px; top: 40px; width: 500px; height: 240px;
    background: radial-gradient(ellipse at center, rgba(255,255,255,0.08), rgba(255,255,255,0) 70%);
  }
  .back-mark {
    position: absolute; left: 50%; top: 70px; transform: translateX(-50%);
    width: 110px; height: 110px; border-radius: 50%; background: #fff;
  }
  .back-name {
    position: absolute; left: 0; right: 0; top: 200px;
    font-family: "Quicksand", sans-serif; font-weight: 500; font-size: 44px; letter-spacing: 0.5px;
  }
  .back-web {
    position: absolute; left: 0; right: 0; top: 312px;
    font-family: "Open Sans", sans-serif; font-size: 17px; letter-spacing: 0.3px;
  }

  /* Front of card */
  .card-front {
    left: 420px; top: 560px;
    background: var(--paper);
  }
  .front-band {
    position: absolute; left: 0; right: 0; bottom: 0; height: 10px; background: var(--blue-deep);
  }
  .front-deco {
    position: absolute; left: 440px; top: 210px; width: 190px; height: 190px;
    border-radius: 50%; background: var(--faint);
  }
  .front-mark {
    position: absolute; left: 110px; top: 24px; width: 96px; height: 96px; border-radius: 50%;
    background: radial-gradient(circle at 40% 35%, var(--blue-light), var(--blue-deep) 80%);
  }
  .front-name {
    position: absolute; left: 32px; top: 140px;
    font-family: "Quicksand", sans-serif; font-weight: 500; font-size: 36px; color: var(--navy);
  }
  .person {
    position: absolute; right: 36px; top: 156px; text-align: right;
    font-family: "Open Sans", sans-serif;
  }
  .person-name { font-size: 21px; font-weight: 600; color: var(--navy); }
  .person-role { font-size: 14px; color: var(--grey); margin-top: 2px; letter-spacing: 0.3px; }
  .rule {
    position: absolute; left: 32px; top: 206px; width: 470px; height: 1px; background: var(--navy);
  }
  .contacts {
    position: absolute; left: 34px; top: 236px; list-style: none;
    font-family: "Open Sans", sans-serif; font-size: 14.5px; color: var(--ink);
  }
  .contacts li { display: flex; align-items: center; height: 21px; }
  .contacts svg { width: 16px; height: 16px; margin-right: 8px; flex: none; }
</style>
</head>
<body>
<div class="canvas">

  <section class="card card-back">
    <div class="world-map" role="img" aria-label="Faint dotted world map"></div>
    <div class="back-mark"></div>
    <div class="back-name">Clearsky Power</div>
    <div class="back-web">www.clearskypower.co.nz</div>
  </section>

  <section class="card card-front">
    <div class="front-deco"></div>
    <div class="front-mark"></div>
    <div class="front-name">Clearsky Power</div>
    <div class="person">
      <div class="person-name">Aria Kent Walsh</div>
      <div class="person-role">General Manager</div>
    </div>
    <div class="rule"></div>
    <ul class="contacts">
      <li>
        <svg viewBox="0 0 16 16"><circle cx="8" cy="8" r="8" fill="#1c4282"/><rect x="5.5" y="3.5" width="5" height="9" rx="1" fill="none" stroke="#fff" stroke-width="1.2"/></svg>
        (03) 418 2096
      </li>
      <li>
        <svg viewBox="0 0 16 16"><circle cx="8" cy="8" r="8" fill="#1c4282"/><rect x="4" y="6.5" width="8" height="5" rx="1" fill="#fff"/><path d="M3.5 6.5 Q8 2.5 12.5 6.5" stroke="#fff" stroke-width="1.4" fill="none"/></svg>
        0508 774 219
      </li>
      <li>
        <svg viewBox="0 0 16 16"><circle cx="8" cy="8" r="8" fill="#1c4282"/><rect x="4" y="5" width="8" height="6" fill="#fff"/><path d="M4 5 L8 8.5 L12 5" stroke="#1c4282" stroke-width="1" fill="none"/></svg>
        hello@clearskypower.co.nz
      </li>
      <li>
        <svg viewBox="0 0 16 16"><circle cx="8" cy="8" r="8" fill="#1c4282"/><circle cx="8" cy="8" r="4.5" fill="none" stroke="#fff" stroke-width="1"/><ellipse cx="8" cy="8" rx="2" ry="4.5" fill="none" stroke="#fff" stroke-width="1"/><line x1="3.5" y1="8" x2="12.5" y2="8" stroke="#fff" stroke-width="1"/></svg>
        www.clearskypower.co.nz
      </li>
      <li>
        <svg viewBox="0 0 16 16"><circle cx="8" cy="8" r="8" fill="#1c4282"/><path d="M8 13 C5 9.5 5 8 5 7 A3 3 0 0 1 11 7 C11 8 11 9.5 8 13Z" fill="#fff"/><circle cx="8" cy="7" r="1.1" fill="#1c4282"/></svg>
        #12 Harbour Lane, Lyttelton, NZ
      </li>
    </ul>
    <div class="front-band"></div>
  </section>

</div>
</body>
</html>
```